Business Card Design

Comprehensive Wealth Management

We provide the following services:
Asset Protection
Trust Administration
Estate Planning - Wills & Trusts
Management of Assets, Stocks, Bonds, ETF's, and Mutual Funds
Tax Planning
Financial Planning
Multi-Generational Planning
Business Planning
Retirement Planning
Risk Management
Hi Designers, please see the attached link for a sample of our website that you can see what we do and you may or may not use the same colors and style. Be creative please.
http://danielforsythe.sitebrook.example/

Target Market(s)

Widows, Trust beneficiaries, Trustees, retirees and those getting ready for retirement

Industry/Entity Type

Business

Contact Information for Business Card

Law Offices of Daniel R. Forsythe
48217 Calloway Avenue, Suite 206
Woodland Hills, California 90000
p: 555.014.2296
f: 555.014.2297
e: dforsythe@meridianwx.example

Daniel R. Forsythe, Esq., CPA, CFP

Colors
0293ce
33a6d7
86cae7
0555a3
3377b5
85acd3
00a990
34b8a4
87d0c7

Requirements
Must have
• I would like a design that really pops. I have a sample brochure that has a molecular structure with the various topics on each molecule. I like the various shades of blue. I can send you the brochure sample if you like.
Nice to have
• Very high end design/logo of some kind that has a modern art look. We primarily work with high net worth and ultra high net worth clients. It should be unique looking. Maybe with pretty greens and blues.

```html
<!DOCTYPE html>
<html lang="en">
<head>
<meta charset="utf-8">
<title>Daniel R. Forsythe — Business Card</title>
<link rel="stylesheet" href="https://fonts.googleapis.com/css2?family=Marcellus&family=Libre+Bodoni:wght@700&family=Arimo:wght@400;700&family=PT+Sans&display=swap">
<style>
  :root {
    --card-navy: #0c2a55;
    --muted-blue: #5f82aa;
    --soft-blue: #3d6796;
    --white: #ffffff;
    --page: #ffffff;
    --shadow: rgba(0, 0, 0, 0.45);
  }
  * { margin: 0; padding: 0; box-sizing: border-box; }
  html, body {
    width: 1200px;
    height: 753px;
    overflow: hidden;
    background: var(--page);
  }
  .canvas { position: relative; width: 1200px; height: 753px; }

  .card {
    position: absolute;
    background: var(--card-navy);
    box-shadow: 5px 6px 7px var(--shadow);
    overflow: hidden;
    color: var(--white);
  }
  .card-front { left: 25px; top: 161px; width: 701px; height: 395px; }
  .card-back  { left: 780px; top: 25px; width: 396px; height: 698px; }

  .molecule-field { position: absolute; }
  .card-front .molecule-field {
    right: 0; top: 0; width: 360px; height: 300px;
    background: radial-gradient(ellipse at 60% 35%, rgba(61,103,150,0.35), rgba(12,42,85,0) 70%);
  }
  .card-back .molecule-field {
    left: 0; bottom: 0; width: 396px; height: 430px;
    background: radial-gradient(ellipse at 55% 60%, rgba(61,103,150,0.35), rgba(12,42,85,0) 70%);
  }

  .firm-label {
    position: absolute; left: 109px; top: 57px;
    font-family: "Marcellus", serif;
    font-size: 51px;
    line-height: 1;
    color: var(--muted-blue);
    white-space: nowrap;
  }
  .attorney-name {
    position: absolute; left: 80px; top: 113px;
    font-family: "Libre Bodoni", serif;
    font-weight: 700;
    font-size: 56px;
    line-height: 1;
    white-space: nowrap;
    letter-spacing: -0.5px;
  }
  .attorney-name .initial { font-size: 92px; }
  .credentials {
    position: absolute; left: 498px; top: 118px;
    font-family: "Arimo", sans-serif;
    font-size: 14px;
    white-space: nowrap;
  }
  .tagline {
    position: absolute; left: 80px; top: 207px;
    font-family: "Marcellus", serif;
    font-size: 30px;
    letter-spacing: 1px;
    color: var(--muted-blue);
    white-space: nowrap;
  }
  .address, .contact {
    position: absolute; top: 287px;
    font-family: "Arimo", sans-serif;
    font-style: normal;
    font-size: 20px;
    line-height: 26px;
    white-space: nowrap;
  }
  .address { left: 79px; }
  .contact { left: 402px; }
  .contact .number { font-weight: 700; letter-spacing: 1.5px; font-size: 21px; }
  .contact .email { font-size: 19px; }

  .services-title {
    position: absolute; left: 0; top: 16px; width: 100%;
    text-align: center;
    font-family: "Marcellus", serif;
    font-size: 36px;
    line-height: 50px;
  }
  .services-list {
    position: absolute; left: 32px; top: 148px;
    list-style: none;
    font-family: "PT Sans", sans-serif;
    font-size: 22.5px;
    line-height: 45.6px;
    white-space: nowrap;
  }
  .services-list li { position: relative; padding-left: 24px; }
  .services-list li::before {
    content: ""; position: absolute; left: 0; top: 16px;
    width: 14px; height: 14px; border-radius: 50%;
    background: var(--white);
  }
</style>
</head>
<body>
<div class="canvas">
  <section class="card card-front">
    <div class="molecule-field" role="img" aria-label="Faint molecular structure pattern in soft blue"></div>
    <p class="firm-label">Law Offices</p>
    <h1 class="attorney-name"><span class="initial">D</span>aniel R. <span class="initial">F</span>orsythe</h1>
    <p class="credentials">Esq., CPA, CFP</p>
    <p class="tagline">Comprehensive Wealth Management</p>
    <address class="address">48217 Calloway Avenue,<br>Suite 206 Woodland Hills,<br>California 90000</address>
    <div class="contact">
      p: <span class="number">555.014.2296</span><br>
      f: <span class="number">555.014.2297</span><br>
      <span class="email">dforsythe@meridianwx.example</span>
    </div>
  </section>

  <section class="card card-back">
    <div class="molecule-field" role="img" aria-label="Faint molecular structure pattern in soft blue"></div>
    <h2 class="services-title">We provide<br>the following services:</h2>
    <ul class="services-list">
      <li>Asset Protection</li>
      <li>Trust Administration</li>
      <li>Estate Planning - Wills &amp; Trusts</li>
      <li>Management of Assets, Stocks,<br>Bonds, ETF's, and Mutual Funds</li>
      <li>Tax Planning</li>
      <li>Financial Planning</li>
      <li>Multi-Generational Planning</li>
      <li>Business Planning</li>
      <li>Retirement Planning</li>
      <li>Risk Management</li>
    </ul>
  </section>
</div>
</body>
</html>
```